Business cards Marta Keller Sport & Events

I need new business cards to match my new logo design for my company called "Marta Keller Sport & Events". I'm based in Germany.
With my company, I offer different services in the context of sport.

Marta Keller owner

Marta Keller Sports & Events
Birkendorfer Weg 14
D-63158 Offenbach

+49 69 / 31 52 94 07
info@marta-keller-sport.example
www.marta-keller-sport.example

Contact Information for Business Card

Marta Keller Inhaberin Marta Keller Sport & Events Birkendorfer Weg 14 D-63158 Offenbach +49 69 / 31 52 94 07 info@marta-keller-sport.example www.marta-keller-sport.example

Requirements
Must have
• Logo | Double sided business card

```html
<!DOCTYPE html>
<html lang="de">
<head>
<meta charset="utf-8">
<title>Marta Keller Sport &amp; Events – Visitenkarte</title>
<link rel="stylesheet" href="https://fonts.googleapis.com/css2?family=Noto+Sans:wght@700&family=Poppins:ital,wght@0,400;0,600;1,400;1,600&display=swap">
<style>
  :root {
    --backdrop: #3a3a3a;
    --card-white: #ffffff;
    --ink: #111111;
    --black: #000000;
    --orange-light: #ffa024;
    --orange-deep: #ef7d1a;
    --mark-grey: rgba(190, 190, 190, 0.75);
  }
  * { margin: 0; padding: 0; box-sizing: border-box; }
  html, body {
    width: 1200px;
    height: 900px;
    overflow: hidden;
    background: var(--backdrop);
  }
  .stage {
    position: relative;
    width: 1200px;
    height: 900px;
  }
  .card {
    position: absolute;
    left: 384px;
    width: 431px;
    height: 246px;
    overflow: hidden;
  }
  /* front side */
  .card-front {
    top: 185px;
    background: var(--card-white);
    display: flex;
    flex-direction: column;
    align-items: center;
    justify-content: center;
    gap: 14px;
    padding-bottom: 24px;
  }
  .brand-dot {
    width: 104px;
    height: 104px;
    border-radius: 50%;
    border: 10px solid var(--orange-light);
  }
  .brand-name {
    font-family: "Poppins", sans-serif;
    font-weight: 600;
    font-size: 19px;
    letter-spacing: 0.04em;
    color: var(--ink);
    white-space: nowrap;
  }
  /* back side */
  .card-back {
    top: 468px;
    background: var(--black);
  }
  .back-diagonal {
    position: absolute;
    inset: 0;
    width: 100%;
    height: 100%;
  }
  .back-ring {
    position: absolute;
    left: 65px;
    top: 134px;
    width: 98px;
    height: 98px;
    border-radius: 50%;
    border: 9px solid var(--mark-grey);
  }
  .holder {
    position: absolute;
    left: 30px;
    top: 26px;
    font-family: "Noto Sans", sans-serif;
    font-weight: 700;
    font-size: 21px;
    line-height: 1.18;
    color: var(--card-white);
    text-transform: uppercase;
  }
  .contact {
    position: absolute;
    left: 238px;
    top: 108px;
    font-family: "Poppins", sans-serif;
    font-size: 11px;
    color: var(--ink);
    white-space: nowrap;
  }
  .address {
    font-style: italic;
    line-height: 18.5px;
    margin-bottom: 20px;
  }
  .phone {
    font-weight: 600;
    font-size: 11.5px;
    line-height: 18px;
  }
  .email, .web {
    font-style: italic;
    font-size: 10.5px;
    line-height: 17px;
  }
</style>
</head>
<body>
<main class="stage">
  <section class="card card-front" aria-label="Vorderseite">
    <div class="brand-dot" aria-hidden="true"></div>
    <p class="brand-name">Marta Keller Sport &amp; Events</p>
  </section>

  <section class="card card-back" aria-label="Rückseite">
    <svg class="back-diagonal" viewBox="0 0 431 246" preserveAspectRatio="none" aria-hidden="true">
      <defs>
        <linearGradient id="orangeFill" x1="0" y1="0" x2="0" y2="1">
          <stop offset="0" stop-color="#ffa024"/>
          <stop offset="1" stop-color="#ef7d1a"/>
        </linearGradient>
      </defs>
      <polygon points="268,0 431,0 431,246 72,246" fill="url(#orangeFill)"/>
    </svg>
    <div class="back-ring" aria-hidden="true"></div>
    <h1 class="holder">Marta Keller<br>Inhaberin</h1>
    <div class="contact">
      <p class="address">Marta Keller Sport &amp; Events<br>Birkendorfer Weg 14<br>D-63158 Offenbach</p>
      <p class="phone">+49 69 / 31 52 94 07</p>
      <p class="email">info@marta-keller-sport.example</p>
      <p class="web">www.marta-keller-sport.example</p>
    </div>
  </section>
</main>
</body>
</html>
```